Web Instant Messenger Design Project

Hello,
The project consist of designing a web instant messenger interface. What we need is a Photoshop file that contains the design elements of this app. (windows, buttons , dropdowns etc)
notes:
- we are looking for the same look and feel as the now closed Tolvia.com
- the name of the app will be quorind.com , or similar.
- the application will be browser based, will cover 100% of the browser area.
- please don't make a "flat" background.
I attached 3 screen captures that shows the graphic elements we need :
img1: -
is the login "page" with username and password fields. There are also a connect & disconnect buttons + a register one
img2:
a) We have the classic friend list that shows who is online and their status. The friend list window can be moved and has 7
buttons (down:add friedn, delete friend, create group,change friend group and create conference / up: conference room list
and mass message buttons)
b) There is a conversation window that can be dragged. The conversation window will keep the private conversations and
conferences as a tab bar. Please note the key field area .
c) Mass Message window - here you can select the group and/or friends, write the message and hit send.
img3
a) on friend list window , when you click one of the down button a new , non movable window will appear. In this window you will have actions corresponding to the button you clicked : add/ delete friend , create conference , etc
b) public room window- is a drag-able window with the conferences you can join.
c)the conversation window with a conference selected. There is a invite buddy drop down, a list of participants and the conversations zone. On participants list there will be a kick and ban button.(not present in this capture)
Updates
When submitting a design please try to provide a mock of the "friend list window". Thank you and sorry if this info comes too late.
Industry/Entity Type
Group
Look and feel
Each slider illustrates characteristics of the customer's brand and the style your logo design should communicate.

```html
<!DOCTYPE html>
<html lang="en">
<head>
<meta charset="utf-8">
<title>quorind – Messenger</title>
<link rel="stylesheet" href="https://fonts.googleapis.com/css2?family=Open+Sans:ital,wght@0,400;0,600;0,700;1,400&display=swap">
<style>
:root{
  --bar-top:#0b6aad;
  --bar-mid:#1b9be0;
  --page:#ebebeb;
  --panel:#ffffff;
  --line:#d6d6d6;
  --head:#f6f6f6;
  --band:#e2e2e2;
  --text:#333333;
  --muted:#8a8a8a;
  --btn-top:#4cb6d8;
  --btn-bot:#2a8fb8;
  --accent:#1f78b4;
  --warn:#e8734c;
  --online:#6aa7c3;
  --offline:#c9c9c9;
  --tip:#3a3a3a;
}
*{box-sizing:border-box;margin:0;padding:0}
html,body{width:1200px;height:700px;overflow:hidden}
body{font-family:"Open Sans",sans-serif;color:var(--text);font-size:13px;position:relative;
  background:repeating-linear-gradient(45deg,#eeeeee 0 2px,#e8e8e8 2px 4px)}
.abs{position:absolute}
.topbar{left:0;top:0;width:1200px;height:37px;background:linear-gradient(90deg,var(--bar-top),var(--bar-mid) 55%,var(--bar-top))}
.brand{left:116px;top:2px;display:flex;align-items:center;gap:8px;color:#fff;font-size:26px;font-weight:700;letter-spacing:.3px}
.brand-mark{width:22px;height:22px;background:#fff}
.panel{background:var(--panel);border:1px solid var(--line);box-shadow:0 1px 3px rgba(0,0,0,.08)}
.panel-head{height:38px;border-bottom:1px solid var(--line);background:var(--head);display:flex;align-items:center;padding-left:14px;gap:10px;font-weight:600;font-size:14px}
.btn{position:absolute;border:1px solid #237fa6;border-radius:3px;background:linear-gradient(var(--btn-top),var(--btn-bot));color:#fff;font-size:13px;font-weight:600;display:flex;align-items:center;justify-content:center}
.select{position:absolute;border:1px solid #d0d0d0;background:linear-gradient(#fff,#f1f1f1);font-size:13px;color:#555;display:flex;align-items:center;padding-left:10px}
.select::after{content:"";position:absolute;right:0;top:0;bottom:0;width:24px;border-left:1px solid #d8d8d8;
  background:linear-gradient(#888,#888) no-repeat center/0 0}
.caret{position:absolute;right:8px;top:50%;margin-top:-2px;border:4px solid transparent;border-top-color:#999}
.group{position:absolute;left:0;width:247px;height:29px;background:var(--band);border-top:1px solid var(--line);border-bottom:1px solid var(--line);font-weight:600;font-size:13px;padding-left:14px;display:flex;align-items:center}
.group span{position:absolute;right:16px;font-weight:700}
.buddy{position:absolute;left:0;width:247px;height:38px;border-bottom:1px solid #e4e4e4;display:flex;align-items:center;padding-left:22px;font-size:14px;
  background:repeating-linear-gradient(45deg,#fafafa 0 2px,#f5f5f5 2px 4px)}
.buddy em{position:absolute;right:42px;font-size:11px;color:var(--muted)}
.buddy svg{position:absolute;right:16px}
.tab{position:absolute;top:97px;height:22px;border:1px solid #d2d2d2;background:linear-gradient(#fdfdfd,#eee);font-size:12px;display:flex;align-items:center}
.tab b{flex:1;text-align:center;font-weight:400}
.tab i{width:24px;height:100%;border-left:1px solid #d2d2d2;display:flex;align-items:center;justify-content:center;font-style:normal;font-weight:700;font-size:12px;color:#777}
.band{background:var(--band);border-top:1px solid var(--line);border-bottom:1px solid var(--line);font-weight:600;font-size:12px;display:flex;align-items:center;padding-left:14px}
.input{position:absolute;border:1px solid #cfcfcf;background:#fff;font-size:13px;display:flex;align-items:center;padding-left:8px}
.close{color:var(--accent);font-weight:700;font-size:14px;position:absolute}
.log p{margin-bottom:9px;font-size:12px}
.log .sys{color:var(--muted)}
.log .who{color:var(--warn)}
.tooltip{left:280px;top:658px;width:121px;height:24px;background:var(--tip);color:#fff;font-size:12px;display:flex;align-items:center;justify-content:center}
</style>
</head>
<body>
<header class="abs topbar">
  <div class="abs brand"><span class="brand-mark"></span>quorind</div>
</header>

<!-- Friend list -->
<section class="abs panel friend-list" style="left:112px;top:50px;width:250px;height:611px">
  <div class="panel-head">
    <svg width="22" height="14" viewBox="0 0 22 14"><circle cx="7" cy="4" r="3.2" fill="#444"/><path d="M1 13c0-4 3-6 6-6s6 2 6 6z" fill="#444"/><circle cx="15" cy="4" r="3" fill="#444"/><path d="M12 8c1-1 2-1 3-1 3 0 6 2 6 6h-7z" fill="#444"/></svg>
    Friend List
  </div>
  <div class="btn" style="left:8px;top:46px;width:111px;height:31px">Mass Message</div>
  <div class="btn" style="left:128px;top:46px;width:111px;height:31px;justify-content:flex-start;padding-left:10px">R........</div>
  <div class="abs" style="left:62px;top:88px;font-size:13px">Status</div>
  <div class="select" style="left:113px;top:85px;width:125px;height:22px;padding-left:32px">
    <svg class="abs" style="left:8px;top:4px" width="18" height="14" viewBox="0 0 18 14"><ellipse cx="7" cy="6" rx="6.5" ry="5" fill="var(--online)"/><ellipse cx="11" cy="8" rx="6" ry="4.5" fill="#8cbad0"/></svg>
    Online<span class="caret"></span>
  </div>

  <div class="group" style="top:117px">Buddies<span>–</span></div>
  <div class="buddy" style="top:147px">Ionut<em>Online</em><svg width="18" height="14" viewBox="0 0 18 14"><ellipse cx="7" cy="6" rx="6.5" ry="5" fill="var(--online)"/><ellipse cx="11" cy="8" rx="6" ry="4.5" fill="#8cbad0"/></svg></div>
  <div class="buddy" style="top:185px">Admin<em>Ofline</em><svg width="18" height="14" viewBox="0 0 18 14"><ellipse cx="7" cy="6" rx="6.5" ry="5" fill="var(--offline)"/><ellipse cx="11" cy="8" rx="6" ry="4.5" fill="#dcdcdc"/></svg></div>
  <div class="buddy" style="top:223px">Cre1<em>Ofline</em><svg width="18" height="14" viewBox="0 0 18 14"><ellipse cx="7" cy="6" rx="6.5" ry="5" fill="var(--offline)"/><ellipse cx="11" cy="8" rx="6" ry="4.5" fill="#dcdcdc"/></svg></div>
  <div class="group" style="top:260px">Kostel<span>–</span></div>
  <div class="buddy" style="top:290px">Big<em>Ofline</em><svg width="18" height="14" viewBox="0 0 18 14"><ellipse cx="7" cy="6" rx="6.5" ry="5" fill="var(--offline)"/><ellipse cx="11" cy="8" rx="6" ry="4.5" fill="#dcdcdc"/></svg></div>
  <div class="buddy" style="top:328px">Bigbig<em>Online</em><svg width="18" height="14" viewBox="0 0 18 14"><ellipse cx="7" cy="6" rx="6.5" ry="5" fill="var(--online)"/><ellipse cx="11" cy="8" rx="6" ry="4.5" fill="#8cbad0"/></svg></div>
  <div class="buddy" style="top:366px">Cre2<em>Ofline</em><svg width="18" height="14" viewBox="0 0 18 14"><ellipse cx="7" cy="6" rx="6.5" ry="5" fill="var(--offline)"/><ellipse cx="11" cy="8" rx="6" ry="4.5" fill="#dcdcdc"/></svg></div>
  <div class="group" style="top:403px">Toba<span>–</span></div>
  <div class="buddy" style="top:433px"></div>
  <div class="buddy" style="top:471px"></div>
  <div class="buddy" style="top:509px"></div>

  <nav class="abs toolbar" style="left:0;top:576px;width:248px;height:34px;border-top:1px solid var(--line);background:#fff">
    <svg class="abs" style="left:16px;top:8px" width="20" height="18" viewBox="0 0 20 18"><circle cx="8" cy="5" r="4" fill="#7db24a"/><path d="M1 17c0-5 3-7 7-7s7 2 7 7z" fill="#7db24a"/><path d="M14 13h6M17 10v6" stroke="#7db24a" stroke-width="2"/></svg>
    <svg class="abs" style="left:64px;top:8px" width="24" height="18" viewBox="0 0 24 18"><circle cx="7" cy="5" r="3.5" fill="#6a8fa3"/><circle cx="14" cy="5" r="3.5" fill="#6a8fa3"/><path d="M0 17c0-5 3-7 7-7s7 2 7 7zM8 17c0-5 3-7 6-7s6 2 6 6z" fill="#6a8fa3"/><path d="M18 14h6M21 11v6" stroke="#6a8fa3" stroke-width="2"/></svg>
    <svg class="abs" style="left:110px;top:8px" width="20" height="18" viewBox="0 0 20 18"><circle cx="8" cy="5" r="4" fill="#e06a3c"/><path d="M1 17c0-5 3-7 7-7s7 2 7 7z" fill="#e06a3c"/><path d="M13 14h7" stroke="#e06a3c" stroke-width="2"/></svg>
    <svg class="abs" style="left:158px;top:8px" width="22" height="18" viewBox="0 0 22 18"><circle cx="8" cy="5" r="4" fill="#9a9a9a"/><path d="M1 17c0-5 3-7 7-7s7 2 7 7z" fill="#9a9a9a"/><path d="M20 12a4 4 0 1 1-2-3" fill="none" stroke="#9a9a9a" stroke-width="2"/></svg>
    <svg class="abs" style="left:205px;top:7px" width="22" height="20" viewBox="0 0 22 20"><circle cx="5" cy="7" r="3" fill="#7db24a"/><circle cx="17" cy="7" r="3" fill="#e0b03c"/><circle cx="11" cy="5" r="3.5" fill="#3d6fc4"/><path d="M4 19c0-5 3-8 7-8s7 3 7 8z" fill="#3d6fc4"/><path d="M14 10l0 9 2-2 2 3 1-1-2-3 3 0z" fill="#fff" stroke="#222" stroke-width=".8"/></svg>
  </nav>
</section>

<!-- Create room popup -->
<section class="abs panel create-room" style="left:118px;top:475px;width:237px;height:148px;box-shadow:0 2px 6px rgba(0,0,0,.2)">
  <div class="panel-head" style="height:38px;gap:12px;padding-left:16px">
    <svg width="17" height="12" viewBox="0 0 17 12"><rect width="17" height="12" fill="#333"/><path d="M0 0l8.5 7L17 0" fill="none" stroke="#fff" stroke-width="1.3"/></svg>
    Create Room
  </div>
  <span class="close" style="right:12px;top:10px">X</span>
  <div class="abs" style="left:9px;top:46px;font-weight:600">Room Name</div>
  <div class="input" style="left:7px;top:67px;width:221px;height:30px">Conefrence</div>
  <div class="btn" style="left:119px;top:104px;width:109px;height:30px">Create Room</div>
</section>

<div class="abs tooltip">Create Conference</div>

<!-- Conversations -->
<section class="abs panel conversations" style="left:371px;top:50px;width:716px;height:611px">
  <div class="panel-head" style="padding-left:18px;gap:12px">
    <svg width="20" height="18" viewBox="0 0 20 18"><path d="M10 1C4.5 1 1 4 1 8c0 2.4 1.4 4.4 3.5 5.6L3.5 17l4.3-2.4c.7.1 1.4.2 2.2.2 5.5 0 9-3 9-7s-3.5-6.8-9-6.8z" fill="#333"/></svg>
    Your Conversations
  </div>
</section>
<div class="tab" style="left:386px;width:93px"><b>Ionut</b><i>×</i></div>
<div class="tab" style="left:487px;width:92px"><b>Cre1</b><i>×</i></div>
<div class="tab" style="left:588px;width:93px"><b>Cre2</b><i>×</i></div>
<div class="tab" style="left:690px;width:93px"><b>Bubu</b><i>×</i></div>
<div class="tab" style="left:791px;width:92px"><b>vasile</b><i>×</i></div>
<div class="tab" style="left:892px;width:93px"><b>Crerm12</b><i>×</i></div>

<div class="abs band" style="left:372px;top:128px;width:714px;height:30px">Multi User Chat</div>

<section class="abs panel participants" style="left:383px;top:167px;width:237px;height:479px">
  <div class="panel-head" style="height:35px;padding-left:9px">Participants</div>
  <span class="close" style="right:12px;top:8px">X</span>
  <div class="abs" style="left:11px;top:45px;font-size:12px">Conefrence</div>
  <div class="abs band" style="left:0;top:345px;width:235px;height:31px;padding-left:15px">Invite Buddies</div>
  <div class="abs" style="left:15px;top:385px;font-weight:600">Select Budy</div>
  <div class="select" style="left:7px;top:408px;width:221px;height:22px">Ionut<span class="caret"></span></div>
  <div class="btn" style="left:119px;top:438px;width:109px;height:29px">Invite</div>
</section>

<div class="abs" style="left:641px;top:178px;font-size:14px">Lable</div>
<div class="abs" style="left:808px;top:176px">Conference Key</div>
<div class="input" style="left:911px;top:173px;width:163px;height:24px"></div>

<div class="abs log" style="left:635px;top:203px;width:440px;height:405px;border:1px solid #cfcfcf;background:#fff;padding:10px 11px">
  <p class="sys">Your joined the room. Conference joined the room</p>
  <p><span class="who">null:</span> This room is locked from entry until configuration is confirmed.</p>
  <p><span class="who">null:</span> This room is now unlocked.</p>
</div>

<div class="input" style="left:635px;top:616px;width:323px;height:31px"></div>
<div class="btn" style="left:966px;top:617px;width:109px;height:30px">Send Message</div>
</body>
</html>
```